Australian Online Training Organisation needs a Website Design

We need a Web Design ideally using a Wordpress Divi template which will represent an Australian Online Training Company.

(Pendlow Online Training)

The website will represent a range of short courses with an emphasis on business, brightnet, leadership etc.

The website will 'shell out' to the third party portal where 'bookings' occur. I am imaging a fantastic looking web design with perhaps 5-6 pages.

I am wondering if a selection of courses including the below list can be incorporated?

The variety of courses include :

Workplace Safety
Sales Training
Leadership
Process Management
Problem Solving
Project Management
Business Planning
Meetings and Events
Emotional Intelligence
Human Resources
Administrative Essentials
Customer Service
Career Development
Conflict Resolution
Train the Trainer
Supervisors and Managers
Internet marketing
Communications
Team Building
Marketing
Finance
Writing
Job Search Skills
Public Speaking
Negotiation Skills
Talent Management
Brightnet Deskline 2016
BDS Preparation for Deskline 2010
Deskline 2013
Deskline 2010
Upgrading to Deskline 2010
Computer Fundamentals
Upgrading to Deskline 2007
Deskline 2003
Deskline 2002
Varlo Deskline X3
Core Essentials
Deskline 2007

Thank you so much for all of the amazing designs we received. We were so happy with so many elements that it was very hard to choose. Our top two were very hard to decide upon but we look forward to working more with both of these talents into the future. Thank you again.

Target Market(s)

Professionals, students and workers who would like to improve their skills with online training in over 500 + courses -

Industry/Entity Type

It Company

Number of Pages Required

5+ page

Font styles to use
Sans Serif

Colors
3276b5
faa54b
0355a3
fac994

Requirements
Must have
• Ideally would use Wordpress theme (Divi for example or other)
• Very smart front end
• Will upload logo soon
• (Pendlow Online Training)
• pendlowonlinetraining.edu.au
• Graphics of 'people' pretty important - with a variety of ages.
Nice to have
• Interesting page
• National presence
• A bit University looking
• Professional
• Graphics of people
• Blog
• Graphics of people
• Age range from job seekers, to business folk, etc

```html
<!DOCTYPE html>
<html lang="en">
<head>
<meta charset="utf-8">
<title>Pendlow Online Training</title>
<link rel="stylesheet" href="https://fonts.googleapis.com/css2?family=Roboto:wght@300;400;500;700;900&display=swap">
<style>
:root{
  --blue:#3276b5;
  --deep:#0355a3;
  --orange:#faa54b;
  --peach:#fac994;
  --navy:#172a46;
  --navy-dark:#0f2138;
  --navy-band:#102a4c;
  --footer:#0b1f3a;
  --bottom:#071528;
  --ink:#2b2f36;
  --muted:#7b818a;
  --line:#e2e4e8;
  --gray:#ecedef;
}
*{box-sizing:border-box;margin:0;padding:0}
html,body{width:1200px;height:4945px;overflow:hidden}
body{font-family:'Roboto',sans-serif;color:var(--ink);background:#fff;font-size:13px;line-height:1.5}
section,header,footer,.topbar{position:relative;width:1200px;overflow:hidden}
.wrap{width:854px;margin:0 auto;position:relative}
.ph{display:block}
.btn{display:inline-block;background:var(--deep);color:#fff;font-size:12px;font-weight:500;padding:0 26px;line-height:34px;border-radius:2px}
.btn.orange{background:var(--orange)}
.title{font-size:20px;font-weight:700;text-transform:uppercase;letter-spacing:.5px;text-align:center;color:var(--ink)}
.title::after{content:"";display:block;width:40px;height:2px;background:var(--blue);margin:8px auto 0}

/* top bar */
.topbar{height:26px;background:var(--deep);color:#dbe6f3;font-size:10.5px}
.topbar .wrap{display:flex;justify-content:space-between;align-items:center;height:26px}
.topbar .group{display:flex;gap:16px;align-items:center}
.dot{width:10px;height:10px;border-radius:50%;background:#8fb3dc;display:inline-block}

/* header */
.site-header{height:124px;background:#fff;z-index:2;overflow:visible}
.nav{display:flex;align-items:center;height:60px;font-size:11px;font-weight:500;text-transform:uppercase;color:var(--ink)}
.nav .left,.nav .right{display:flex;gap:26px;flex:1}
.nav .right{justify-content:flex-end;align-items:center}
.search{width:36px;height:36px;background:var(--orange);display:flex;align-items:center;justify-content:center}
.brand{position:absolute;left:367px;top:-26px;width:120px;height:150px;background:#fff;box-shadow:0 3px 10px rgba(0,0,0,.15);display:flex;align-items:flex-end;justify-content:center;padding-bottom:22px;z-index:3}
.brand span{font-size:19px;font-weight:700;color:var(--deep);letter-spacing:2px}
.brand i{position:absolute;top:40px;left:43px;width:34px;height:34px;background:var(--deep)}

/* hero */
.hero{margin-top:-64px;height:524px}
.hero-photo{position:absolute;inset:0;background:linear-gradient(110deg,#d9cbb6 0%,#b79c7e 35%,#6f8aa8 65%,#c7b49a 100%)}
.hero-card{position:absolute;left:198px;top:84px;width:297px;height:390px;background:rgba(255,255,255,.93);padding:26px 24px;text-align:center}
.hero-card h2{font-size:17px;font-weight:700;text-align:left}
.stars{display:flex;gap:3px;align-items:center;margin-top:4px;font-size:10px;color:var(--muted)}
.hero-card p{font-size:11px;color:var(--muted);margin:18px 0 24px;line-height:1.6}
.from{font-size:12px;color:var(--muted);letter-spacing:1px}
.price{font-size:36px;font-weight:700;color:var(--ink);line-height:1.1;margin-bottom:26px}
.hero-card .btn{width:100%;font-size:11px;text-transform:uppercase}

/* services */
.services{height:527px;padding-top:40px;text-align:center}
.welcome{font-size:20px;font-weight:400;margin-bottom:20px}
.service-cards{display:flex;gap:36px;margin-top:44px;text-align:left}
.service{flex:1}
.service .ph{height:127px;display:flex;align-items:center;justify-content:center;color:#fff;font-size:18px;font-weight:700}
.service .count{font-size:11px;color:var(--muted);margin:8px 0 6px}
.service .count b{color:var(--ink)}
.service li{list-style:none;display:flex;align-items:center;gap:8px;font-size:12px;margin-bottom:5px}
.services .btn{margin-top:40px}

/* courses */
.courses{height:1023px;background:linear-gradient(#fff 0 83px,var(--gray) 83px)}
.desk{position:absolute;left:150px;top:0;width:900px;height:190px;background:radial-gradient(ellipse at 30% 45%,#d9dadd 0,rgba(217,218,221,0) 28%),radial-gradient(ellipse at 68% 50%,#cfd2d6 0,rgba(207,210,214,0) 26%),linear-gradient(90deg,rgba(236,237,239,0),#e4e5e8 20%,#e4e5e8 80%,rgba(236,237,239,0))}
.courses-head{padding-top:280px;text-align:center}
.courses-head .sub{font-size:11px;color:var(--muted);margin-top:10px}
.tabs{display:flex;justify-content:center;gap:30px;margin-top:40px;font-size:12px;color:var(--muted)}
.tabs span{padding-bottom:6px}
.tabs .on{color:var(--ink);border-bottom:2px solid var(--blue)}
.grid{display:grid;grid-template-columns:repeat(4,1fr);gap:16px;margin-top:34px}
.card{background:#fff;height:205px}
.card .ph{height:98px}
.card .body{padding:9px 10px}
.card h3{font-size:12px;font-weight:700}
.card p{font-size:10px;color:var(--muted);line-height:1.4;margin-top:3px}
.meta{display:flex;gap:10px;font-size:9.5px;color:var(--muted);margin-top:8px;align-items:center}
.meta i{display:inline-block;width:8px;height:8px;border-radius:50%;background:var(--orange);margin-right:3px}
.courses .center{text-align:center;margin-top:40px}

/* about */
.about{height:352px;display:flex}
.about .ph{width:600px;height:352px;background:linear-gradient(135deg,#8a6b4f,#c4a98a 45%,#5b6f86)}
.about-text{flex:1;background:var(--navy);color:#c9d3e2;padding:26px 170px 0 20px}
.about-text h2,.why h2{color:#fff;font-size:18px;font-weight:700;text-transform:uppercase}
.about-text h2::after,.why h2::after,.testi h2::after{content:"";display:block;width:34px;height:2px;background:var(--orange);margin-top:6px}
.about-text p{font-size:11px;line-height:1.6;margin:14px 0 18px}

/* why + testimonials */
.why-row{height:422px;display:flex}
.why{width:600px;background:var(--navy-dark);padding:36px 60px 0 171px;color:#9fb0c7}
.why h3{color:#fff;font-size:12px;font-weight:700;margin-top:20px}
.why p{font-size:10.5px;line-height:1.5}
.testi{flex:1;padding:36px 175px 0 20px}
.testi h2{font-size:18px;font-weight:700;text-transform:uppercase}
.quote{font-size:11px;color:var(--muted);margin-top:26px;line-height:1.5}
.person{display:flex;align-items:center;gap:10px;margin-top:12px;padding-bottom:16px;border-bottom:1px solid var(--line)}
.avatar{width:36px;height:36px;border-radius:50%;background:#c9ced6;flex:none}
.person b{display:block;font-size:11px;text-transform:uppercase}
.person small{font-size:10px;color:var(--muted)}
.dots{display:flex;gap:6px;justify-content:center;margin-top:22px}
.dots i{width:7px;height:7px;border-radius:50%;background:#cfd3d9}
.dots i.on{background:var(--blue)}

/* blog */
.blog{height:521px;background:#f3f4f6;padding-top:46px}
.blog-grid{display:flex;gap:20px;margin-top:44px}
.post{flex:1;background:#fff;height:323px}
.post .ph{height:149px}
.post .body{padding:14px 14px}
.post h3{font-size:14px;font-weight:700}
.post p{font-size:10.5px;color:var(--muted);margin-top:6px;line-height:1.5}
.post .meta{border-top:1px solid var(--line);padding-top:10px;margin-top:16px}

/* newsletter */
.newsletter{height:122px;background:var(--deep);color:#fff}
.newsletter .wrap{display:flex;align-items:center;height:122px}
.newsletter .copy{display:flex;gap:16px;align-items:center;flex:1;padding-left:60px}
.newsletter h3{font-size:13px;font-weight:700;text-transform:uppercase}
.newsletter small{font-size:10.5px;color:#bcd1ea}
.field{width:300px;height:32px;background:#fff;color:#9aa1ab;font-size:11px;padding:0 12px;line-height:32px}
.subscribe{width:102px;height:32px;background:var(--orange);font-size:11px;line-height:32px;text-align:center}

/* mission */
.mission{height:676px;text-align:center;padding-top:40px}
.mission h2{font-size:28px;font-weight:400;line-height:1.35;color:var(--ink)}
.mission p{font-size:11px;color:var(--muted);margin:24px auto 16px;width:420px}
.people{position:absolute;left:180px;top:246px;width:840px;height:410px;border-radius:6px;
  background:
    linear-gradient(180deg,rgba(255,255,255,.55) 0%,rgba(255,255,255,0) 30%,rgba(255,255,255,0) 75%,rgba(255,255,255,.6) 100%),
    linear-gradient(90deg,#d98a8a 0%,#3d4654 16%,#7fa6c9 32%,#e7c58f 46%,#3276b5 60%,#9a8fc4 74%,#e0a36a 87%,#7cc1a8 100%)}

/* partners */
.partners{height:437px;background:linear-gradient(180deg,#1a3a63 0%,var(--navy-band) 100%);color:#fff;text-align:center;padding-top:146px}
.partners h2{font-size:22px;font-weight:700;text-transform:uppercase}
.partners .sub{font-size:13px;color:#b7c4d6;margin-top:2px}
.logos{display:flex;justify-content:space-between;align-items:center;margin-top:88px;font-size:20px;font-weight:700}
.partners .note{font-size:11px;color:#a9b8cc;margin-top:60px;display:flex;gap:6px;justify-content:center;align-items:center}

/* footer */
.site-footer{height:222px;background:var(--footer);color:#a9b8cc;padding-top:22px}
.cols{display:flex}
.col{font-size:10.5px}
.col h4{color:#fff;font-size:13px;font-weight:700;margin-bottom:12px}
.col li{list-style:none;display:flex;gap:8px;align-items:flex-start;margin-bottom:7px}
.input{width:186px;height:20px;background:#1c3352;margin-bottom:6px;font-size:9.5px;line-height:20px;padding:0 6px;color:#7f92ac}
.input.tall{height:40px}
.send{width:50px;height:20px;background:var(--orange);color:#fff;font-size:9.5px;line-height:20px;text-align:center}
.map{width:186px;height:130px;background:linear-gradient(135deg,#dfe3e1,#c9d2cc)}
.social{display:flex;gap:10px}
.social i{width:14px;height:14px;border-radius:50%;background:#6f86a6}
.foot-brand{font-size:20px;font-weight:700;color:#3b5275;letter-spacing:2px;margin-top:60px}
.bottom{height:33px;background:var(--bottom);color:#8094ae;font-size:10px}
.bottom .wrap{display:flex;justify-content:space-between;align-items:center;height:33px;width:1040px}
.up{width:28px;height:28px;background:var(--orange);display:flex;align-items:center;justify-content:center}
</style>
</head>
<body>

<div class="topbar">
  <div class="wrap">
    <div class="group">
      <span>✉ info@pendlow.edu.au</span>
      <span>☎ 1800 000 417</span>
    </div>
    <div class="group">
      <span>Login | Register</span>
      <span class="group" style="gap:6px"><i class="dot"></i><i class="dot"></i><i class="dot"></i><i class="dot"></i></span>
    </div>
  </div>
</div>

<header class="site-header">
  <div class="wrap">
    <nav class="nav">
      <div class="left"><span>About</span><span>Courses ▾</span><span>For Employers</span></div>
      <div style="width:150px"></div>
      <div class="right"><span>Testimonials</span><span>Blog</span><span>Contact Us</span>
        <span class="search"><svg width="14" height="14" viewBox="0 0 14 14"><circle cx="6" cy="6" r="4.5" fill="none" stroke="#fff" stroke-width="1.8"/><line x1="9.3" y1="9.3" x2="13" y2="13" stroke="#fff" stroke-width="1.8"/></svg></span>
      </div>
    </nav>
    <div class="brand"><i></i><span>PENDLOW</span></div>
  </div>
</header>

<section class="hero">
  <div class="hero-photo ph" role="img" aria-label="Photo of smiling young students gathered around a laptop outdoors"></div>
  <div class="hero-card">
    <h2>Project Management Course</h2>
    <div class="stars">
      <svg width="70" height="12" viewBox="0 0 70 12" fill="#faa54b"><g id="s"><polygon points="6,0 7.6,4.2 12,4.4 8.6,7.2 9.7,11.6 6,9.1 2.3,11.6 3.4,7.2 0,4.4 4.4,4.2"/></g><use href="#s" x="14"/><use href="#s" x="28"/><use href="#s" x="42"/><use href="#s" x="56"/></svg>
      <span>(245 Excellent review)</span>
    </div>
    <p>Learn how to plan, run and close projects with confidence. Build real skills in scope, budget and team leadership at your own pace.</p>
    <div class="from">STARTING FROM</div>
    <div class="price">$120.00</div>
    <span class="btn">Join the course</span>
  </div>
</section>

<section class="services">
  <div class="wrap">
    <h1 class="welcome">Welcome to Pendlow Online Training</h1>
    <h2 class="title">Our Services</h2>
    <div class="service-cards">
      <div class="service">
        <div class="ph" role="img" aria-label="Photo of a business team meeting" style="background:linear-gradient(135deg,#7d8a99,#b9a48c)">Business</div>
        <div class="count">Learn from <b>154</b> courses including:</div>
        <ul>
          <li><svg width="12" height="12"><rect width="12" height="12" rx="2" fill="#3276b5"/></svg>Workplace Safety</li>
          <li><svg width="12" height="12"><rect width="12" height="12" rx="2" fill="#3276b5"/></svg>Sales Training</li>
          <li><svg width="12" height="12"><rect width="12" height="12" rx="2" fill="#3276b5"/></svg>Business Planning</li>
        </ul>
      </div>
      <div class="service">
        <div class="ph" role="img" aria-label="Photo of a person working at a desk computer" style="background:linear-gradient(135deg,#a88f78,#d7c4a8)">Brightnet</div>
        <div class="count">Learn from <b>120</b> courses including:</div>
        <ul>
          <li><svg width="12" height="12"><rect width="12" height="12" rx="2" fill="#faa54b"/></svg>Brightnet Deskline 2016</li>
          <li><svg width="12" height="12"><rect width="12" height="12" rx="2" fill="#faa54b"/></svg>Varlo Deskline X3</li>
          <li><svg width="12" height="12"><rect width="12" height="12" rx="2" fill="#faa54b"/></svg>Core Essentials</li>
        </ul>
      </div>
      <div class="service">
        <div class="ph" role="img" aria-label="Photo of a leader speaking to a group" style="background:linear-gradient(135deg,#4f5d6e,#9aa6b2)">Leadership</div>
        <div class="count">Learn from <b>147</b> courses including:</div>
        <ul>
          <li><svg width="12" height="12"><rect width="12" height="12" rx="2" fill="#0355a3"/></svg>Process Management</li>
          <li><svg width="12" height="12"><rect width="12" height="12" rx="2" fill="#0355a3"/></svg>Problem Solving</li>
          <li><svg width="12" height="12"><rect width="12" height="12" rx="2" fill="#0355a3"/></svg>Human Resources</li>
        </ul>
      </div>
    </div>
    <span class="btn">Start your free trial</span>
  </div>
</section>

<section class="courses">
  <div class="desk ph" role="img" aria-label="Illustration of a desk top with laptop, coffee cup, notebook, glasses and stationery"></div>
  <div class="wrap">
    <div class="courses-head">
      <h2 class="title">Browse Our Top Courses</h2>
      <div class="sub">We teach what you need. Pick a course and start learning today!</div>
      <div class="tabs"><span class="on">Business</span><span>Brightnet</span><span>Leadership</span></div>
    </div>
    <div class="grid">
      <div class="card"><div class="ph" role="img" aria-label="Photo of workers in safety helmets" style="background:linear-gradient(135deg,#e0b94a,#8c7a5e)"></div><div class="body"><h3>Workplace Safety</h3><p>Keep your team safe with proven habits, clear rules and simple checks every day.</p><div class="meta"><span><i></i>24</span><span><i></i>18</span><span><i></i>9</span></div></div></div>
      <div class="card"><div class="ph" role="img" aria-label="Video still of a sales presenter" style="background:linear-gradient(135deg,#6e7f92,#b7a58f)"></div><div class="body"><h3>Sales Training</h3><p>Learn to open, pitch and close deals with confidence and a friendly approach.</p><div class="meta"><span><i></i>31</span><span><i></i>12</span><span><i></i>7</span></div></div></div>
      <div class="card"><div class="ph" role="img" aria-label="Photo of a business plan notebook" style="background:linear-gradient(135deg,#e9e6e1,#b8b2a8)"></div><div class="body"><h3>Business Planning</h3><p>Turn ideas into a clear plan with goals, budgets and steps you can follow.</p><div class="meta"><span><i></i>19</span><span><i></i>15</span><span><i></i>6</span></div></div></div>
      <div class="card"><div class="ph" role="img" aria-label="Graphic of online marketing icons" style="background:linear-gradient(135deg,#2f6fb0,#8fb7de)"></div><div class="body"><h3>Internet Marketing</h3><p>Grow your reach online with search, social and email campaigns that work.</p><div class="meta"><span><i></i>27</span><span><i></i>21</span><span><i></i>8</span></div></div></div>
      <div class="card"><div class="ph" role="img" aria-label="Graphic of office admin skills" style="background:linear-gradient(135deg,#f2c36b,#8fb56a)"></div><div class="body"><h3>Administrative Essentials</h3><p>Master the daily tasks that keep an office running smooth and on time.</p><div class="meta"><span><i></i>22</span><span><i></i>14</span><span><i></i>5</span></div></div></div>
      <div class="card"><div class="ph" role="img" aria-label="Video still of a marketing lesson" style="background:linear-gradient(135deg,#5c6b7a,#a89a86)"></div><div class="body"><h3>Marketing</h3><p>Understand your market, shape your message and win loyal customers.</p><div class="meta"><span><i></i>26</span><span><i></i>17</span><span><i></i>9</span></div></div></div>
      <div class="card"><div class="ph" role="img" aria-label="Video still of a finance lesson on screen" style="background:linear-gradient(135deg,#3e5f86,#9cb3c9)"></div><div class="body"><h3>Finance</h3><p>Read reports, manage cash flow and make sound money choices at work.</p><div class="meta"><span><i></i>18</span><span><i></i>11</span><span><i></i>4</span></div></div></div>
      <div class="card"><div class="ph" role="img" aria-label="Chalkboard graphic about career growth" style="background:linear-gradient(135deg,#2d3b3a,#5d6f6c)"></div><div class="body"><h3>Career Development</h3><p>Map your next move, grow key skills and stand out to employers.</p><div class="meta"><span><i></i>29</span><span><i></i>20</span><span><i></i>10</span></div></div></div>
    </div>
    <div class="center"><span class="btn">View All Courses</span></div>
  </div>
</section>

<section class="about">
  <div class="ph" role="img" aria-label="Photo of two smiling students in front of a university building"></div>
  <div class="about-text">
    <h2>About Us</h2>
    <p>Pendlow Online Training is one of Australia's leading providers of flexible and affordable online professional development programs, with over 500 online courses now available.<br>Our range of self-paced online courses are delivered completely online via our e-learning system 24/7.<br>We offer a range of popular online courses in accounting, finance, bookkeeping, management, marketing, information technology, project management and more. Our online courses are industry relevant and are designed to help you achieve your career goals.</p>
    <span class="btn orange">Read More</span>
  </div>
</section>

<section class="why-row">
  <div class="why">
    <h2>Why Pendlow Online?</h2>
    <h3>Flexible</h3>
    <p>Study anytime and anywhere on a learning platform built to fit around your work, family and life.</p>
    <h3>Value</h3>
    <p>Our courses cost less than classroom training, with no travel and no hidden fees. Pay once and keep access to your notes and progress.</p>
    <h3>Experience</h3>
    <p>Pendlow is one of Australia's most trusted providers of online training for businesses and people.</p>
  </div>
  <div class="testi">
    <h2>Testimonials</h2>
    <div class="quote">"This package has helped me grow my practice. The course was easy to follow and worth it."</div>
    <div class="person"><span class="avatar" role="img" aria-label="Portrait of the reviewer"></span><div><b>Rhea Calloway</b><small>Clinic Manager</small></div></div>
    <div class="quote">"Clear lessons, helpful tutors and a smart system. I finished two courses and got a new role soon after."</div>
    <div class="person"><span class="avatar" role="img" aria-label="Portrait of the reviewer"></span><div><b>Owen Harlow</b><small>Sales Team Lead</small></div></div>
    <div class="dots"><i class="on"></i><i></i><i></i></div>
  </div>
</section>

<section class="blog">
  <div class="wrap">
    <h2 class="title">From The Blog</h2>
    <div class="blog-grid">
      <div class="post"><div class="ph" role="img" aria-label="Photo of graduates in caps and gowns" style="background:linear-gradient(135deg,#3a3f49,#a8927a)"></div><div class="body"><h3>Nemo enim ipsam voluptatem</h3><p>Quia voluptas sit aspernatur aut odit aut fugit, sed quia consequuntur magni dolores eos qui ratione sequi.</p><div class="meta"><span><i></i>Mara Quint</span><span><i></i>28th June 2016</span><span><i></i>10</span></div></div></div>
      <div class="post"><div class="ph" role="img" aria-label="Photo of a mug beside a sign about online courses" style="background:linear-gradient(135deg,#7a5a3e,#d6c2a4)"></div><div class="body"><h3>Nemo enim ipsam voluptatem</h3><p>Quia voluptas sit aspernatur aut odit aut fugit, sed quia consequuntur magni dolores eos qui ratione sequi.</p><div class="meta"><span><i></i>Mara Quint</span><span><i></i>28th June 2016</span><span><i></i>10</span></div></div></div>
      <div class="post"><div class="ph" role="img" aria-label="Graphic about talent management benefits" style="background:linear-gradient(135deg,#1f3b5c,#5a7ea6)"></div><div class="body"><h3>Nemo enim ipsam voluptatem</h3><p>Quia voluptas sit aspernatur aut odit aut fugit, sed quia consequuntur magni dolores eos qui ratione sequi.</p><div class="meta"><span><i></i>Mara Quint</span><span><i></i>28th June 2016</span><span><i></i>10</span></div></div></div>
    </div>
  </div>
</section>

<section class="newsletter">
  <div class="wrap">
    <div class="copy">
      <svg width="28" height="22" viewBox="0 0 28 22"><rect x="1" y="1" width="26" height="20" fill="none" stroke="#fff" stroke-width="2"/><polyline points="1,1 14,12 27,1" fill="none" stroke="#fff" stroke-width="2"/></svg>
      <div><h3>Stay updated with Pendlow</h3><small>Get our latest courses and news each month</small></div>
    </div>
    <div class="field">Email</div>
    <div class="subscribe">Subscribe</div>
  </div>
</section>

<section class="mission">
  <h2>We provide universal access to the world's best education<br>&amp; offer courses for anyone</h2>
  <p>Learn new skills from home with flexible courses built by experts. Study at your pace and get support whenever you need it.</p>
  <span class="btn">Join The Course</span>
  <div class="people ph" role="img" aria-label="Illustration of a row of learners of different ages, from students and graduates to business people and a child"></div>
</section>

<section class="partners">
  <div class="wrap">
    <h2>You're in great company</h2>
    <div class="sub">Trusted by</div>
    <div class="logos"><span>Steady Reach</span><span>Quillmart</span><span>Parcelo</span><span>Brightnet</span><span>Coralbay</span></div>
    <div class="note"><svg width="10" height="10" viewBox="0 0 12 12" fill="#fac994"><polygon points="6,0 7.6,4.2 12,4.4 8.6,7.2 9.7,11.6 6,9.1 2.3,11.6 3.4,7.2 0,4.4 4.4,4.2"/></svg>Plus tens of thousands of other companies in 154 countries worldwide</div>
  </div>
</section>

<footer class="site-footer">
  <div class="wrap cols">
    <div class="col" style="width:218px">
      <h4>Contact Us</h4>
      <ul>
        <li><svg width="9" height="12" viewBox="0 0 9 12"><path d="M4.5 0a4.5 4.5 0 0 1 4.5 4.5C9 8 4.5 12 4.5 12S0 8 0 4.5A4.5 4.5 0 0 1 4.5 0z" fill="#faa54b"/></svg><span>24 Harbour Lane,<br>Kellview QLD 4350</span></li>
        <li><svg width="10" height="10"><rect width="10" height="10" rx="2" fill="#faa54b"/></svg>1800 000 417</li>
        <li><svg width="10" height="10"><rect width="10" height="10" rx="2" fill="#faa54b"/></svg>info@pendlow.edu.au</li>
      </ul>
    </div>
    <div class="col" style="width:221px">
      <h4>Quick Contact</h4>
      <div class="input">Name</div>
      <div class="input">Email</div>
      <div class="input tall">Message</div>
      <div class="send">Submit</div>
    </div>
    <div class="col" style="width:230px">
      <h4>Locate Us</h4>
      <div class="map ph" role="img" aria-label="Street map showing the office location"></div>
    </div>
    <div class="col">
      <h4>Follow Us</h4>
      <div class="social"><i></i><i></i><i></i><i></i></div>
      <div class="foot-brand">PENDLOW</div>
    </div>
  </div>
</footer>

<div class="bottom">
  <div class="wrap">
    <span>© Copyright Pendlow Online Training. All rights reserved.</span>
    <span class="up"><svg width="12" height="8" viewBox="0 0 12 8"><polyline points="1,7 6,2 11,7" fill="none" stroke="#fff" stroke-width="2"/></svg></span>
  </div>
</div>

</body>
</html>
```